【概要】 求人サイトに掲載するサムネイル画像作成依頼です。 素敵なデザインがあれば複数採用いたします。 【 依頼内容 】 ・サイズ:横900x縦600 ・ターゲット:20代~50代向けの求人 【 入れていただきたい文言】※これ以外の文言は入れないでください ・固定ルート+体力負担なし+無理な運転はさせない社風=長く働ける環境です! ・6tドライバー募集 ・月給35万円可能 【画像に関して】 注:こちらの画像サイズ、データで提出できる方のみお願い致します。 ★「横900ピクセルx縦600ピクセル」(PNGファイル×1、PSDデータ×1) ・配信時は制作したバナーがスマホの画面幅程度に縮小されて表示されます。テキストの可読性を考慮して制作お願いします。 ・文字を記入する際、できれば画像としてではなく、フォトショップのテキストを使用していただければと存じます。 ・テキストデータはアウトライン化されていない、後から編集できる状態での納品をお願いいたします。(イラストレーターNG) ・フォントやあしらいにフリー素材を使用する場合は著作権に抵触しないものをご利用下さい。 【重要な指定】 ※目を惹きクリックされるインパクトのあるバナーをお願い致します。 サイト内で使用するものなので「こちらをクリック」「詳細はこちら」などのフレーズはなしでお願いいたします。 ・添付画像をご使用ください ・添付画像は反転しないで下さい 【ご注意】 ※他で登録されているデザインや商標の転用など、他社の知的財産権を侵すことNG ※他のクライアントへ既に提案した内容の転用などNG ※ご提案頂きましたバナー案について、SNSへの投稿・Webサイトへのアップ等NG →ポートフォリオ・コンペ提案作品一覧にもアップNGです。 アップする際には、社名を削除し、写真はフリー素材に差し替えてください。 ※今後、画像を再利用する可能性がございます。 ※WEBサイトで他の求人に使用することがあります。 【対応時間】 平日:9時半~18時半 その他ご質問、ご不明点等ありましたら、気軽にお問い合わせください。 見やすく、素敵なデザインをお待ちしております! |
どの案も素敵でしたが、こちらの作品が一番イメージに合っておりました。
皆様ご提案ありがとうございました。どれも個性的でよい提案ばかりでした。また機会がありましたら依頼させていただきますのでよろしくお願いします。

```html
<!DOCTYPE html>
<html lang="ja">
<head>
<meta charset="utf-8">
<title>6tドライバー募集</title>
<link rel="stylesheet" href="https://fonts.googleapis.com/css2?family=Noto+Sans+JP:wght@700;900&display=swap">
<style>
  :root {
    --red: #e60012;
    --deep-red: #8a0008;
    --yellow: #fff100;
    --navy: #142a6e;
    --navy-dark: #0a1740;
    --white: #ffffff;
    --bg-light: #eef0f3;
    --bg-mid: #d6dae0;
  }
  * { margin: 0; padding: 0; box-sizing: border-box; }
  html, body { width: 1200px; height: 800px; overflow: hidden; }
  body {
    font-family: "Noto Sans JP", sans-serif;
    background: var(--bg-light);
  }
  .banner {
    position: relative;
    width: 1200px;
    height: 800px;
    overflow: hidden;
    background: linear-gradient(180deg, var(--bg-light), var(--bg-mid));
  }
  .staff-photo {
    position: absolute;
    left: 560px; top: 104px;
    width: 640px; height: 696px;
    background: linear-gradient(160deg, #c9ced6 0%, #8e97a6 45%, #2c3550 100%);
  }
  .header-band {
    position: absolute;
    left: 0; top: 0;
    width: 1200px; height: 100px;
    background: var(--red);
    border-bottom: 6px solid var(--white);
    box-shadow: 0 6px 0 rgba(0,0,0,.35);
    display: flex; align-items: center; justify-content: center;
    z-index: 2;
  }
  .headline {
    font-weight: 900;
    font-size: 96px;
    line-height: 1;
    color: var(--yellow);
    -webkit-text-stroke: 10px var(--deep-red);
    paint-order: stroke fill;
    text-shadow: 4px 5px 0 #3a0003;
    transform: scaleX(1.32);
    letter-spacing: -2px;
  }
  .features {
    position: absolute;
    left: 40px; top: 110px;
    width: 700px; height: 120px;
  }
  .feature-text {
    font-weight: 900;
    fill: var(--white);
    text-anchor: middle;
  }
  .tagline {
    position: absolute;
    left: 70px; top: 228px;
    font-weight: 900;
    font-size: 50px;
    line-height: 1;
    color: var(--navy);
    -webkit-text-stroke: 10px var(--white);
    paint-order: stroke fill;
    transform: skewX(-6deg);
    letter-spacing: -1px;
  }
  .salary-label {
    position: absolute;
    left: 30px; top: 506px;
    width: 120px; height: 186px;
    background: var(--white);
    border: 8px solid var(--red);
    display: flex; flex-direction: column; align-items: center; justify-content: center;
    font-weight: 900;
    font-size: 76px;
    line-height: 1.02;
    color: var(--red);
  }
  .salary-amount {
    position: absolute;
    left: 150px; top: 398px;
    font-weight: 900;
    font-size: 330px;
    line-height: 1;
    letter-spacing: -10px;
    color: var(--yellow);
    -webkit-text-stroke: 18px var(--red);
    paint-order: stroke fill;
    text-shadow: 8px 8px 0 var(--deep-red);
    transform: scaleX(1.04);
    transform-origin: left center;
  }
  .salary-unit {
    position: absolute;
    left: 662px; top: 572px;
    font-weight: 900;
    font-size: 128px;
    line-height: 1;
    letter-spacing: -4px;
    color: var(--red);
    -webkit-text-stroke: 14px var(--white);
    paint-order: stroke fill;
    text-shadow: 4px 4px 0 rgba(0,0,0,.35);
  }
</style>
</head>
<body>
<div class="banner">
  <div class="staff-photo" role="img" aria-label="トラックの前で肩を組んで笑顔を見せる作業着姿のドライバー2人の写真"></div>

  <header class="header-band">
    <h1 class="headline">6tドライバー募集</h1>
  </header>

  <svg class="features" viewBox="0 0 700 120" aria-label="固定ルート＋体力負担なし＋無理な運転はさせない社風">
    <g stroke="var(--white)" stroke-width="6" fill="var(--navy)">
      <polygon points="45,6 175,6 210,60 175,114 45,114 10,60"/>
      <polygon points="285,6 415,6 450,60 415,114 285,114 250,60"/>
      <polygon points="520,6 650,6 685,60 650,114 520,114 485,60"/>
    </g>
    <g fill="var(--red)" stroke="var(--white)" stroke-width="4">
      <path d="M218,48 h12 v-14 h12 v14 h12 v12 h-12 v14 h-12 v-14 h-12 z"/>
      <path d="M454,48 h12 v-14 h12 v14 h12 v12 h-12 v14 h-12 v-14 h-12 z"/>
    </g>
    <text class="feature-text" x="110" y="54" font-size="30">固定</text>
    <text class="feature-text" x="110" y="90" font-size="30">ルート</text>
    <text class="feature-text" x="350" y="54" font-size="30">体力</text>
    <text class="feature-text" x="350" y="90" font-size="30">負担なし</text>
    <text class="feature-text" x="585" y="54" font-size="24">無理な運転は</text>
    <text class="feature-text" x="585" y="86" font-size="24">させない社風</text>
  </svg>

  <p class="tagline">長く働ける環境です!</p>

  <div class="salary-label"><span>月</span><span>給</span></div>
  <div class="salary-amount">35</div>
  <div class="salary-unit">万円可能</div>
</div>
</body>
</html>
```